Business card for a boutique travel agency VELARIEN

we need a business card design - double sided. We would like to have a very elegant, sophisticated but modern design. we are travel consultants and our business focus is Europe, mainly the city of Paris. We would like to receive designs in white and silver, black color but if you are confident that we should pick up a color to make it different and more beautful...go ahead! We are going to give business cards to our clients and business partners. It is important to be perceived as elegant, modern and trustful. Please check jpg references.

Target Market(s)

Velarien primary clients are individuals, couples and affinity groups of high-net-worth who travel for leisure at least once per year. Seeking the ultimate travel experience, the target clients demand the finest quality activities and accommodations accompanied by a superior level of service.

Industry/Entity Type

Travel Industry

Contact Information for Business Card

Lucinda Farrow
- lucinda@velarien-example.com
- +55 11 98347.2516
- velarien-example.com
- unique travel experiences (we would like to see this signature printed as a detail)

Font styles to use
Sans Serif

Colors

Designer to choose colors to be used in the design.

Requirements
Must have
• the Velarien logo that I have attached
Nice to have
• we would like to have some nice detail, something different that shows that we care about,... we are detail oriented.
Should not have
• decorative fonts

```html
<!DOCTYPE html>
<html lang="en">
<head>
<meta charset="UTF-8">
<title>Velarien – Business Card</title>
<link href="https://fonts.googleapis.com/css2?family=Jost:wght@300;400;600&family=Cormorant+Garamond:ital,wght@1,500&display=swap" rel="stylesheet">
<style>
  :root {
    --backdrop: #232323;
    --card: #1b1b1c;
    --card-edge: #2c2c2d;
    --gloss: #070707;
    --ink-light: #f2f2f2;
    --ink-soft: #d4d4d4;
  }
  * { margin: 0; padding: 0; box-sizing: border-box; }
  html, body {
    width: 960px;
    height: 1200px;
    overflow: hidden;
    background: var(--backdrop);
  }
  .sheet {
    position: relative;
    width: 960px;
    height: 1200px;
    display: flex;
    flex-direction: column;
    align-items: center;
    justify-content: center;
    gap: 110px;
  }
  .card {
    position: relative;
    width: 700px;
    height: 400px;
    background: radial-gradient(ellipse at 60% 40%, #222224 0%, var(--card) 70%);
    border: 1px solid var(--card-edge);
    box-shadow: 0 18px 40px rgba(0,0,0,0.45);
  }
  .wordmark {
    font-family: 'Jost', sans-serif;
    font-weight: 300;
    text-transform: uppercase;
  }
  .card--front .wordmark {
    position: absolute;
    left: 0; right: 0;
    top: 50%;
    transform: translateY(-50%);
    text-align: center;
    font-size: 44px;
    letter-spacing: 0.32em;
    padding-left: 0.32em;
    color: var(--gloss);
    text-shadow: 0 1px 0 rgba(255,255,255,0.08);
  }
  .card--back .wordmark {
    position: absolute;
    top: 56px;
    right: 60px;
    font-size: 28px;
    letter-spacing: 0.3em;
    color: var(--ink-light);
  }
  .contact {
    position: absolute;
    left: 56px;
    bottom: 50px;
    font-family: 'Jost', sans-serif;
    color: var(--ink-soft);
  }
  .contact__name {
    font-weight: 600;
    font-size: 22px;
    color: var(--ink-light);
    margin-bottom: 8px;
    letter-spacing: 0.02em;
  }
  .contact__line {
    font-weight: 400;
    font-size: 16px;
    line-height: 1.45;
    letter-spacing: 0.02em;
  }
  .signature {
    position: absolute;
    right: 56px;
    bottom: 110px;
    font-family: 'Cormorant Garamond', serif;
    font-style: italic;
    font-weight: 500;
    font-size: 24px;
    word-spacing: 0.35em;
    color: var(--ink-light);
  }
</style>
</head>
<body>
  <main class="sheet">
    <section class="card card--front" aria-label="Card front">
      <h1 class="wordmark">Velarien</h1>
    </section>

    <section class="card card--back" aria-label="Card back">
      <p class="wordmark">Velarien</p>
      <p class="signature">unique travel experiences</p>
      <address class="contact" style="font-style:normal">
        <p class="contact__name">Lucinda Farrow</p>
        <p class="contact__line">+55 11 98347.2516</p>
        <p class="contact__line">lucinda@velarien-example.com</p>
        <p class="contact__line">velarien-example.com</p>
      </address>
    </section>
  </main>
</body>
</html>
```